KAZ Freightworks #ALLKAZ Business Cards & Letterhead

I am looking to business cards designed for our organization. We are currently undergoing a small re-branding that is taking place. Our organization is called KAZ Freightworks and we are headquartered in Phoenix, AZ. We primarily provide transportation and logistics services to the Meridel Parcel Bureau who is our largest customer. I would like to see a design that incorporates name, title, contact info, website, and address (this will be different depending on the employee). I would also like to see some color on the business card using our logo colors or a variation. I would like our logo on the back of the business card with the website displayed. The final design should communicate that we are a next generation transportation operate that focuses on being driver-first, customer-centric, innovative, and sustainable.We would also like our #ALLKAZ catch phrase incorporated as well.
Updates

Decision maker traveling outside of the country until Monday, November 25th.

Target Market(s)

Transportation & Logistics

Industry/Entity Type

Trucking Company

Contact Information for Business Card

-First and Last Name
-Position Title
-Contact Phone
-Contact Email
-Physical Address

Font styles to use
Serif

Colors

Designer to choose colors to be used in the design.

Requirements
Must have
• -KAZ logo prominently displayed
• -#ALLKAZ catch phrase used
• -Some amount of color, design gradient, etc.
• -Logo on the back with website listed (https://www.kazfreightco.example)

```html
<!DOCTYPE html>
<html lang="en">
<head>
<meta charset="utf-8">
<title>KAZ Freightworks Business Card</title>
<link href="https://fonts.googleapis.com/css2?family=Tinos:wght@400;700&display=swap" rel="stylesheet">
<style>
  :root {
    --stage: #d9d9d9;
    --teal: #023a47;
    --green: #7dc242;
    --white: #ffffff;
    --ink: #333333;
  }
  html, body { margin: 0; padding: 0; overflow: hidden; }
  body {
    width: 1200px; height: 1020px;
    background: var(--stage);
    position: relative;
    font-family: "Tinos", "Times New Roman", serif;
  }
  .card {
    position: absolute;
    left: 272px;
    width: 656px; height: 376px;
    border-radius: 20px;
    overflow: hidden;
  }
  .card-front { top: 88px; background: var(--teal); }
  .card-back { top: 514px; background: var(--white); }

  .front-mark {
    position: absolute;
    left: 238px; top: 50px;
    width: 180px; height: 180px;
    box-sizing: border-box;
    border: 5px solid var(--white);
    border-radius: 50%;
    display: flex; align-items: center; justify-content: center;
    color: var(--white);
    font-weight: 700; font-size: 58px; letter-spacing: 2px;
  }
  .front-tagline {
    position: absolute; left: 0; right: 0; top: 252px; margin: 0;
    text-align: center; color: var(--green);
    font-weight: 700; font-size: 24px; letter-spacing: 3px;
  }
  .front-website {
    position: absolute; left: 0; right: 0; top: 292px; margin: 0;
    text-align: center; color: var(--white);
    font-size: 17px; letter-spacing: 0.5px;
  }

  .back-mark {
    position: absolute;
    left: 182px; top: 125px;
    width: 126px; height: 126px;
    box-sizing: border-box;
    border: 4px solid var(--green);
    border-radius: 50%;
    display: flex; align-items: center; justify-content: center;
    color: var(--teal);
    font-weight: 700; font-size: 42px; letter-spacing: 1px;
  }
  .divider {
    position: absolute;
    left: 327px; top: 123px;
    width: 2px; height: 131px;
    background: var(--teal);
  }
  .person-name {
    position: absolute; left: 344px; top: 117px; margin: 0;
    color: var(--teal); font-weight: 700; font-size: 26px; letter-spacing: 0.5px;
  }
  .person-title {
    position: absolute; left: 345px; top: 150px; margin: 0;
    color: var(--ink); font-size: 18px;
  }
  .contact-list {
    position: absolute; left: 352px; top: 193px;
    list-style: none; margin: 0; padding: 0;
    color: var(--ink); font-size: 17px; line-height: 22px;
  }
  .contact-list li { display: flex; align-items: center; gap: 8px; }
  .contact-list svg { width: 12px; height: 12px; fill: var(--teal); flex: none; }
  .address {
    position: absolute; left: 0; right: 0; top: 310px;
    text-align: center; color: var(--ink); font-size: 17px;
  }
  .address svg { display: block; margin: 0 auto 3px; width: 11px; height: 15px; fill: var(--teal); }
</style>
</head>
<body>
  <section class="card card-front">
    <div class="front-mark">KAZ</div>
    <p class="front-tagline">#ALLKAZ</p>
    <p class="front-website">https://www.kazfreightco.example</p>
  </section>

  <section class="card card-back">
    <div class="back-mark">KAZ</div>
    <div class="divider"></div>
    <h1 class="person-name">Daniel Orrin</h1>
    <p class="person-title">Owner</p>
    <ul class="contact-list">
      <li>
        <svg viewBox="0 0 24 24"><path d="M6.6 10.8a15.1 15.1 0 0 0 6.6 6.6l2.2-2.2c.3-.3.7-.4 1-.2 1.1.4 2.3.6 3.6.6.6 0 1 .4 1 1V20c0 .6-.4 1-1 1C10.6 21 3 13.4 3 4c0-.6.4-1 1-1h3.5c.6 0 1 .4 1 1 0 1.3.2 2.5.6 3.6.1.3 0 .7-.2 1z"/></svg>
        (602) 555-0148
      </li>
      <li>
        <svg viewBox="0 0 24 24"><path d="M2 5h20v14H2zm2 2v.5l8 5 8-5V7zm0 2.8V17h16V9.8l-8 5z"/></svg>
        hello@kazfreightco.example
      </li>
      <li>
        <svg viewBox="0 0 24 24"><path d="M12 2a10 10 0 1 0 0 20 10 10 0 0 0 0-20zm-1 17.9A8 8 0 0 1 4.1 11H8v2l3 3zm6.9-2.6c-.3-.8-1-1.3-1.9-1.3h-1v-3c0-.6-.4-1-1-1H8v-2h2c.6 0 1-.4 1-1V7h2c1.1 0 2-.9 2-2v-.4a8 8 0 0 1 2.9 12.7z"/></svg>
        www.kazfreightco.example
      </li>
    </ul>
    <div class="address">
      <svg viewBox="0 0 12 16"><path d="M6 0a6 6 0 0 0-6 6c0 4.5 6 10 6 10s6-5.5 6-10a6 6 0 0 0-6-6zm0 8.5A2.5 2.5 0 1 1 6 3.5a2.5 2.5 0 0 1 0 5z"/></svg>
      1840 W Ridgeway Dr, Phoenix AZ 85007
    </div>
  </section>
</body>
</html>
```